RMT Electrical Business Card Design

Have a logo to use, just looking for design around this, would like green theme, would like symbols in place of phone, fax, email etc.

Business

Contact Information for Business Card

RMT Electrical, Simon Ashcroft, simon@rmtelectrical-example.com.au, www.rmtelectrical-example.com.au, mobile 0412 555 019, phone (07) 3555 0142, fax (07) 3555 0142, facebook and linkedin
addresses

```html
<!DOCTYPE html>
<html lang="en">
<head>
<meta charset="utf-8">
<title>RMT Electrical Business Card</title>
<link rel="stylesheet" href="https://fonts.googleapis.com/css2?family=Didact+Gothic&display=swap">
<style>
  :root {
    --page: #e9e6e1;
    --card-white: #fbfbfb;
    --card-white-edge: #e4e4e4;
    --card-dark: #262626;
    --card-dark-edge: #161616;
    --ink-dark: #2e2e2e;
    --ink-light: #f2f2f2;
    --accent: #6fd37a;
    --shadow: rgba(0, 0, 0, 0.22);
  }
  * { box-sizing: border-box; margin: 0; padding: 0; }
  html, body {
    width: 704px;
    height: 1200px;
    overflow: hidden;
    background: var(--page);
    font-family: "Didact Gothic", "Century Gothic", sans-serif;
  }
  .sheet {
    width: 704px;
    height: 1200px;
    display: flex;
    flex-direction: column;
    justify-content: space-around;
    align-items: center;
  }
  .card {
    width: 560px;
    height: 320px;
    border-radius: 18px;
    position: relative;
    box-shadow: 0 14px 30px var(--shadow);
  }
  .card-front {
    background: linear-gradient(160deg, var(--card-white) 55%, var(--card-white-edge));
    display: flex;
    align-items: center;
    justify-content: center;
  }
  .brand {
    display: flex;
    align-items: center;
    gap: 16px;
  }
  .brand-dot {
    width: 46px;
    height: 46px;
    border-radius: 50%;
    background: var(--accent);
  }
  .brand-name {
    font-size: 54px;
    color: var(--ink-dark);
    letter-spacing: 0.5px;
  }
  .card-back {
    background: linear-gradient(160deg, #2f2f2f, var(--card-dark) 55%, var(--card-dark-edge));
    padding: 48px 44px 0 0;
    display: flex;
    flex-direction: column;
    align-items: flex-end;
  }
  .person-name {
    font-size: 22px;
    color: var(--accent);
    margin-right: 120px;
    margin-bottom: 34px;
  }
  .contact-list {
    list-style: none;
    display: flex;
    flex-direction: column;
    align-items: flex-end;
    gap: 8px;
  }
  .contact-item {
    display: flex;
    align-items: center;
    gap: 10px;
    font-size: 15px;
    color: var(--ink-light);
  }
  .contact-icon {
    width: 14px;
    height: 14px;
    flex: none;
  }
  .contact-label {
    font-size: 11px;
    color: var(--accent);
    width: 14px;
    text-align: center;
  }
</style>
</head>
<body>
<main class="sheet">
  <section class="card card-front" aria-label="Card front">
    <div class="brand">
      <span class="brand-dot"></span>
      <span class="brand-name">RMT Electrical</span>
    </div>
  </section>

  <section class="card card-back" aria-label="Card back">
    <h1 class="person-name">Simon Ashcroft</h1>
    <ul class="contact-list">
      <li class="contact-item">(07) 3555 0142
        <svg class="contact-icon" viewBox="0 0 14 14" aria-label="phone"><path d="M3 1h2.5l1 3-1.5 1a7 7 0 0 0 4 4l1-1.5 3 1V11a2 2 0 0 1-2 2A11 11 0 0 1 1 3a2 2 0 0 1 2-2z" fill="var(--accent)"/></svg>
      </li>
      <li class="contact-item">0412 555 019
        <svg class="contact-icon" viewBox="0 0 14 14" aria-label="mobile"><rect x="3.5" y="1" width="7" height="12" rx="1.3" fill="none" stroke="var(--accent)" stroke-width="1.4"/><circle cx="7" cy="10.8" r="0.8" fill="var(--accent)"/></svg>
      </li>
      <li class="contact-item">(07) 3555 0142
        <span class="contact-label">FX</span>
      </li>
      <li class="contact-item">simon@rmtelectrical-example.com.au
        <svg class="contact-icon" viewBox="0 0 14 14" aria-label="email"><rect x="1" y="3" width="12" height="8.5" rx="1" fill="var(--accent)"/><path d="M1.5 3.5 7 8l5.5-4.5" fill="none" stroke="var(--card-dark)" stroke-width="1.1"/></svg>
      </li>
      <li class="contact-item">www.rmtelectrical-example.com.au
        <svg class="contact-icon" viewBox="0 0 14 14" aria-label="website"><circle cx="7" cy="7" r="5.6" fill="none" stroke="var(--accent)" stroke-width="1.3"/><ellipse cx="7" cy="7" rx="2.4" ry="5.6" fill="none" stroke="var(--accent)" stroke-width="1"/><path d="M1.5 7h11" stroke="var(--accent)" stroke-width="1"/></svg>
      </li>
    </ul>
  </section>
</main>
</body>
</html>
```